Business Book - Quiet Mornings at the Ledger Desk (Finding Calm Among Daily Numbers)

I'm looking for a cover that appeals to successful business people who are used to reading business titles.

The cover should feel familiar and fit in with the existing canon of bestselling business books with a vibrant, but professional look (see attached).

I want my book to stand out, but not to be frivolous. Abstract is probably best. Or close to it.

Please feel free to use my brand colours, or go with something else -

Teal
HEX #199BAB
25 / 155 / 171

Coral
HEX #EE786E
238 / 120/ 110

I don't want to include anything connected with robots or gendered assistants/business people. Or headsets.

It's only 24 hours which is mental

```html
<!DOCTYPE html>
<html lang="en">
<head>
<meta charset="utf-8">
<title>Quiet Mornings at the Ledger Desk — Book Cover</title>
<link rel="stylesheet" href="https://fonts.googleapis.com/css2?family=Mulish:wght@600;700;800&display=swap">
<style>
  :root {
    --backdrop: #e3e3e3;
    --cover-teal: #1a7b89;
    --cover-teal-deep: #0f5a67;
    --cover-teal-light: #5aa9b5;
    --title-ink: #dfe7ea;
    --title-accent: #cdd283;
    --subtitle-ink: #e8eef0;
  }
  html, body {
    margin: 0;
    padding: 0;
    width: 1200px;
    height: 1200px;
    overflow: hidden;
    background: var(--backdrop);
  }
  .canvas {
    position: relative;
    width: 1200px;
    height: 1200px;
    background: var(--backdrop);
  }
  .book-cover {
    position: absolute;
    left: 222px;
    top: 50px;
    width: 756px;
    height: 1100px;
    overflow: hidden;
    background: var(--cover-teal);
    font-family: "Mulish", "Helvetica Neue", Arial, sans-serif;
  }
  .cover-artwork {
    position: absolute;
    inset: 0;
    width: 756px;
    height: 1100px;
    display: block;
  }
  .cover-title {
    position: relative;
    z-index: 1;
    margin: 0;
    padding-top: 40px;
    text-align: center;
    font-weight: 700;
    font-size: 62px;
    line-height: 86px;
    color: var(--title-ink);
    letter-spacing: 0.3px;
  }
  .cover-title .title-line { display: block; }
  .cover-title .title-accent { color: var(--title-accent); }
  .cover-subtitle {
    position: absolute;
    z-index: 1;
    left: 0;
    right: 0;
    top: 996px;
    margin: 0;
    text-align: center;
    font-weight: 800;
    font-size: 29px;
    color: var(--subtitle-ink);
    letter-spacing: 0.2px;
  }
</style>
</head>
<body>
  <main class="canvas">
    <article class="book-cover">
      <svg class="cover-artwork" viewBox="0 0 756 1100" role="img" aria-label="Line illustration of simple desks receding diagonally across the cover with a soft shadow band">
        <defs>
          <linearGradient id="base-tone" x1="0" y1="0" x2="0.6" y2="1">
            <stop offset="0" stop-color="var(--cover-teal)"/>
            <stop offset="0.5" stop-color="#1a7684"/>
            <stop offset="1" stop-color="var(--cover-teal-deep)"/>
          </linearGradient>
          <radialGradient id="glow" cx="0.12" cy="0.7" r="0.55">
            <stop offset="0" stop-color="var(--cover-teal-light)" stop-opacity="0.85"/>
            <stop offset="1" stop-color="var(--cover-teal-light)" stop-opacity="0"/>
          </radialGradient>
          <linearGradient id="shadow-band" x1="0" y1="0" x2="1" y2="1">
            <stop offset="0" stop-color="#0c4f5b" stop-opacity="0.15"/>
            <stop offset="1" stop-color="#0c4f5b" stop-opacity="0.6"/>
          </linearGradient>
        </defs>
        <rect class="artwork-base" width="756" height="1100" fill="url(#base-tone)"/>
        <rect class="artwork-glow" width="756" height="1100" fill="url(#glow)"/>
        <polygon class="artwork-band" points="0,330 756,760 756,1100 560,1100 0,640" fill="url(#shadow-band)"/>
      </svg>
      <h1 class="cover-title">
        <span class="title-line">Quiet Mornings</span>
        <span class="title-line">at the</span>
        <span class="title-line title-accent">Ledger Desk</span>
      </h1>
      <p class="cover-subtitle">‘Finding Calm Among Daily Numbers’</p>
    </article>
  </main>
</body>
</html>
```